Company or website name
- www.brambletalentpartners.com
- Links to the website
- Bramble Talent Partners
- Describe your company and organization and target audience
- We are a full service executive recruiting and staffing company. We work within all vertical markets within the US.
- The design should have the following
- Please ensure to include colors of the logo but feel free to include other colors as well to enhance the brochure. I'm looking for a single 8.5 x 11 inch brochure with front and back. The back will have more specific information while the front will be more a space for photos and general information on our company.
- Other Facts

```html
<!DOCTYPE html>
<html lang="en">
<head>
<meta charset="utf-8">
<title>Bramble Talent Partners – Brochure</title>
<link href="https://fonts.googleapis.com/css2?family=Open+Sans:ital,wght@0,400;0,600;0,700;0,800;1,400&display=swap" rel="stylesheet">
<style>
:root{
  --navy:#14366b;
  --blue:#1a6fb5;
  --sky:#2a9be0;
  --ink:#4a4f57;
  --muted:#8a9099;
  --ghost:#e3e6ea;
  --paper:#ffffff;
  --backdrop:#e6e8eb;
  --photo-a:#d9dfe6;
  --photo-b:#b8c4d2;
}
*{box-sizing:border-box;margin:0;padding:0}
html,body{width:1200px;height:900px;overflow:hidden}
body{background:var(--backdrop);font-family:"Open Sans",Arial,sans-serif;color:var(--ink);position:relative}

.page{position:absolute;width:380px;height:492px;background:var(--paper);box-shadow:0 6px 18px rgba(0,0,0,.18);overflow:hidden}
.page-band{position:absolute;left:0;right:0;bottom:0;height:16px;background:var(--navy)}

/* ---------- Front cover ---------- */
.cover{left:20px;top:204px}
.cover-photo{position:absolute;left:0;top:0;width:380px;height:300px;background:linear-gradient(180deg,var(--photo-a) 0%,var(--photo-b) 60%,#ffffff 100%)}
.cover-headline{position:absolute;left:24px;top:312px;font-weight:800;font-size:40px;line-height:1;color:var(--navy);letter-spacing:-.5px}
.cover-headline .accent{color:var(--sky)}
.cover-subhead{position:absolute;left:24px;top:354px;font-size:24px;color:var(--ink);font-weight:400}
.cover-tagline{position:absolute;left:24px;top:388px;font-size:11px;color:var(--muted)}
.brand{display:flex;align-items:center;gap:6px;font-family:"Open Sans",Arial,sans-serif;font-weight:700;color:var(--navy);white-space:nowrap}
.brand-dot{width:14px;height:14px;border-radius:50%;background:var(--navy)}
.cover .brand{position:absolute;left:24px;top:432px;font-size:12px}
.cover-contact{position:absolute;right:22px;top:424px;font-size:6.5px;line-height:1.6;color:var(--muted);text-align:right}

/* ---------- Inside spread ---------- */
.spread{position:absolute;left:420px;top:204px;width:760px;height:492px}
.inside-left{left:0;top:0}
.inside-right{left:380px;top:0;box-shadow:6px 6px 18px rgba(0,0,0,.18)}
.fold{position:absolute;left:379px;top:0;width:2px;height:492px;background:linear-gradient(90deg,rgba(0,0,0,.08),rgba(0,0,0,0));z-index:3}

.ghost-word{position:absolute;font-weight:800;font-size:52px;color:var(--ghost);letter-spacing:1px;white-space:nowrap;transform-origin:left top;transform:rotate(-90deg)}
.inside-left .ghost-word{left:4px;top:470px}
.inside-right .ghost-word{left:324px;top:470px}

.section-title{font-weight:800;font-size:22px;color:var(--sky);letter-spacing:.5px;margin-bottom:8px}
.column{position:absolute;font-size:6.4px;line-height:1.5}
.column h3{font-size:7.6px;font-weight:700;color:var(--navy);margin:7px 0 3px;display:flex;gap:4px;align-items:flex-start}
.column h3::before{content:"";flex:none;width:6px;height:6px;background:var(--navy);margin-top:1px}
.column p{margin-bottom:3px}
.employers-column{left:62px;top:26px;width:140px}
.seekers-column{left:190px;top:66px;width:150px}

.feature-panel{position:absolute;color:#fff;font-size:6.4px;line-height:1.5}
.feature-panel h2{font-weight:600;font-size:11px;color:#bfe3fb;margin-bottom:6px}
.feature-panel p{margin-bottom:5px}
.panel-shadow{position:absolute;background:#dfe3e8}
.process-shadow{left:212px;top:36px;width:160px;height:230px;clip-path:polygon(14% 0,100% 6%,100% 100%,0 92%)}
.process-panel{left:206px;top:26px;width:160px;height:228px;padding:30px 16px 0 30px;background:linear-gradient(180deg,var(--navy) 0%,var(--blue) 100%);clip-path:polygon(14% 0,100% 8%,100% 100%,0 90%)}
.why-shadow{left:20px;top:64px;width:160px;height:232px;clip-path:polygon(0 4%,100% 0,88% 92%,0 100%)}
.why-panel{left:14px;top:54px;width:160px;height:232px;padding:22px 24px 0 14px;background:linear-gradient(180deg,var(--navy) 0%,var(--blue) 100%);clip-path:polygon(0 6%,100% 0,86% 90%,0 100%)}

.team-photo{position:absolute;left:214px;top:300px;width:220px;height:176px;background:linear-gradient(180deg,#eef2f6 0%,#c7d3e0 55%,#9fb2c7 100%);z-index:2}
.inside-left .brand{position:absolute;left:250px;top:274px;font-size:9px;z-index:4}
.inside-left .brand-dot{width:11px;height:11px}
</style>
</head>
<body>

<section class="page cover">
  <div class="cover-photo" role="img" aria-label="Photo of business colleagues smiling and shaking hands across a desk"></div>
  <h1 class="cover-headline">WE'VE <span class="accent">GOT</span> IT.</h1>
  <p class="cover-subhead">Whatever you're looking for.</p>
  <p class="cover-tagline">At Bramble we exceed our clients' expectations.</p>
  <div class="brand"><span class="brand-dot"></span>Bramble Talent Partners</div>
  <div class="cover-contact">
    1200 Market Street, Suite 400<br>Springfield, IL 62701<br>(555) 014-2200<br>www.brambletalentpartners.com
  </div>
  <div class="page-band"></div>
</section>

<section class="spread">
  <div class="page inside-left">
    <div class="ghost-word">EMPLOYERS</div>
    <div class="column employers-column">
      <h2 class="section-title">EMPLOYERS</h2>
      <h3>Contingency Search – Direct Hire/Permanent</h3>
      <p>We identify, screen and present qualified candidates for your permanent openings. You pay a fee only when a hire is made, so your risk stays low from the first call.</p>
      <h3>Retained Search/Executive Search – Direct Hire/Permanent</h3>
      <p>For senior and hard to fill roles we commit a dedicated team to a focused search, mapping the market and guiding you through every step to a confident offer.</p>
      <h3>Temporary and Contract Staffing</h3>
      <p>When workloads rise or projects begin, we supply skilled professionals ready to contribute at once. We handle payroll, taxes and benefits so your team can focus on results.</p>
      <h3>Temporary/Contract-to-Hire</h3>
      <p>Try a candidate on the job before you decide. This flexible option lets both sides confirm the fit and makes the move to a permanent role simple and smooth.</p>
    </div>
    <div class="panel-shadow process-shadow"></div>
    <div class="feature-panel process-panel">
      <h2>Our Process</h2>
      <p>We begin by learning your business, culture and goals. Our recruiters then search our network, screen each candidate and present only those who match your needs.</p>
      <p>We stay in touch after the placement to make sure the match is working for everyone.</p>
    </div>
    <div class="brand"><span class="brand-dot"></span>Bramble Talent Partners</div>
    <div class="page-band"></div>
  </div>

  <div class="page inside-right">
    <div class="ghost-word">SEEKERS</div>
    <div class="panel-shadow why-shadow"></div>
    <div class="feature-panel why-panel">
      <h2>Why choose us?</h2>
      <p>Our expertise in recruiting and staffing in administrative, financial, legal, human resources, information technology, healthcare and property management helps you meet all competitive challenges.</p>
      <p>Our clients tell us we contribute to their success by working under the highest ethical standards and providing exceptional, innovative solutions. Customer satisfaction is our top priority.</p>
      <p>Finding the right candidates is just the start of our partnership with you.</p>
    </div>
    <div class="column seekers-column">
      <h2 class="section-title">SEEKERS</h2>
      <h3>Our Client Companies</h3>
      <p>Our clients range from growing local firms to national leaders in every market. We keep your search confidential and share openings that fit your skills and goals.</p>
      <h3>Our Candidates</h3>
      <p>We work with talented people at every stage of their careers. Our recruiters take time to understand what you want and help you find the right next step.</p>
      <h3>Your Resume</h3>
      <p>Send us your resume and a recruiter will review it within two business days. If we do not have a match today, we keep your profile on file for new openings.</p>
    </div>
    <div class="page-band"></div>
  </div>

  <div class="fold"></div>
  <div class="team-photo" role="img" aria-label="Photo of a smiling team of business professionals standing together"></div>
</section>

</body>
</html>
```